Corrigan Construction Law P.A.

Business Card with Corporate Logo. For a law firm specializing in construction law.

need address, telephone, email and website. Also, have an elegant and conservative logo.

Logo so it is RBN.

Full name "Gordon T. Corrigan

Under my name title "Attorney at Law"

Under title "Board Certified in Construction Law"

PA in email is lower case

Add logo to back side of card

Mix in a bit of gold color into card to go with the green

Some color on bottom
Updates

Target Market(s)

legal

Industry/Entity Type

Construction

Contact Information for Business Card

I like it -- edits: 1. add "L" to logo so it is RBN. 2. add my full name "Gordon T. Business Card with Corporate Logo. For a law firm specializing in construction law.

Logo so it is RBN.

PA in email is lower case

Font styles to use
Serif

Colors
00a990
f78f20

Requirements
Must have
• Conservative legal designed logo for construction market
• Address:
• Corrigan Construction Law, P.A.
• 4150 Meadowlark Ave North, Ste B4
• Jacksonville, Florida 32217
• Main: 904-555-3172
• Direct: 904-555-8410
• Fax: 904-555-8410
• gt@corriganpa-example.com
• www.corriganbuildlaw-example.com
Nice to have
• Catchy conservative logo on card
Should not have
• Flashy

```html
<!DOCTYPE html>
<html lang="en">
<head>
<meta charset="utf-8">
<title>Corrigan Construction Law P.A. — Business Card</title>
<link rel="stylesheet" href="https://fonts.googleapis.com/css2?family=Sorts+Mill+Goudy&family=Carlito&display=swap">
<style>
  :root {
    --maroon: #4c0a1e;
    --maroon-icon: #5c1024;
    --gold: #f2a81d;
    --cream: #f4ece6;
    --band: #ffffff;
    --ink: #1c1c1c;
    --rule: #9a6a78;
  }
  html, body {
    margin: 0;
    padding: 0;
    overflow: hidden;
    background: #ffffff;
  }
  .card {
    position: relative;
    width: 1200px;
    height: 588px;
    background: var(--maroon);
    overflow: hidden;
    font-family: "Sorts Mill Goudy", "Goudy Old Style", serif;
  }
  .brand-mark {
    position: absolute;
    left: 0;
    right: 0;
    top: 70px;
    text-align: center;
    color: var(--gold);
    font-family: "Sorts Mill Goudy", serif;
    font-size: 96px;
    letter-spacing: 6px;
    line-height: 1;
  }
  .attorney-name,
  .attorney-title {
    position: absolute;
    left: 0;
    right: 0;
    text-align: center;
    color: var(--cream);
    font-size: 35px;
    letter-spacing: 1px;
    line-height: 1;
  }
  .attorney-name { top: 260px; }
  .name-rule {
    position: absolute;
    left: 398px;
    width: 352px;
    top: 300px;
    height: 1px;
    background: var(--rule);
  }
  .attorney-title { top: 307px; }
  .certification {
    position: absolute;
    left: 0;
    right: 0;
    top: 368px;
    text-align: center;
    color: var(--cream);
    font-size: 41px;
    letter-spacing: 1px;
    line-height: 1;
  }
  .contact-band {
    position: absolute;
    left: 0;
    top: 445px;
    width: 1200px;
    height: 122px;
    background: var(--band);
  }
  .contact-item {
    position: absolute;
    display: flex;
    align-items: center;
    font-family: "Carlito", "Calibri", sans-serif;
    font-size: 20px;
    color: var(--ink);
  }
  .contact-item svg { flex: none; }
  .contact-item .label { margin-left: 20px; }
  .item-address { left: 50px; top: 22px; }
  .item-phone { left: 50px; top: 66px; }
  .item-web { left: 676px; top: 22px; }
  .item-firm { left: 676px; top: 66px; }
  .item-web .label, .item-firm .label { margin-left: 38px; }
  .bottom-strip {
    position: absolute;
    left: 0;
    top: 567px;
    width: 1200px;
    height: 21px;
    background: var(--maroon);
  }
</style>
</head>
<body>
<main class="card">
  <div class="brand-mark">RBN</div>

  <div class="attorney-name">Gordon T. Corrigan</div>
  <div class="name-rule"></div>
  <div class="attorney-title">Attorney at Law</div>
  <div class="certification">Board Certified in Construction Law</div>

  <section class="contact-band">
    <div class="contact-item item-address">
      <svg width="56" height="30" viewBox="0 0 56 30" aria-hidden="true">
        <path d="M2 15 L28 2 L54 15 L48 15 L28 5 L8 15 Z" fill="var(--maroon-icon)"/>
        <path d="M12 15 L28 7 L44 15 L44 28 L33 28 L33 20 L23 20 L23 28 L12 28 Z" fill="var(--maroon-icon)"/>
      </svg>
      <span class="label">Company Location/address</span>
    </div>
    <div class="contact-item item-phone">
      <svg width="56" height="30" viewBox="0 0 56 30" aria-hidden="true">
        <path d="M4 10 C14 2 42 2 52 10 L50 16 L40 14 L39 9 C32 7 24 7 17 9 L16 14 L6 16 Z" fill="var(--maroon-icon)" transform="rotate(-12 28 14)"/>
        <path d="M10 22 C14 27 20 28 24 26" stroke="var(--maroon-icon)" stroke-width="4" fill="none" stroke-linecap="round"/>
      </svg>
      <span class="label">Company&nbsp; phone number/ contact number</span>
    </div>
    <div class="contact-item item-web">
      <svg width="50" height="38" viewBox="0 0 50 38" aria-hidden="true">
        <rect x="2" y="2" width="46" height="34" fill="none" stroke="var(--maroon-icon)" stroke-width="2"/>
        <circle cx="25" cy="19" r="11" fill="none" stroke="var(--maroon-icon)" stroke-width="2"/>
        <ellipse cx="25" cy="19" rx="5" ry="11" fill="none" stroke="var(--maroon-icon)" stroke-width="1.6"/>
        <line x1="14" y1="19" x2="36" y2="19" stroke="var(--maroon-icon)" stroke-width="1.6"/>
        <line x1="16" y1="13" x2="34" y2="13" stroke="var(--maroon-icon)" stroke-width="1.4"/>
        <line x1="16" y1="25" x2="34" y2="25" stroke="var(--maroon-icon)" stroke-width="1.4"/>
      </svg>
      <span class="label">Company Website</span>
    </div>
    <div class="contact-item item-firm">
      <svg width="46" height="28" viewBox="0 0 46 28" aria-hidden="true">
        <rect x="1" y="2" width="44" height="24" rx="2" fill="var(--maroon-icon)"/>
        <path d="M3 4 L23 17 L43 4" stroke="#c9a9b2" stroke-width="1.6" fill="none"/>
      </svg>
      <span class="label">Corrigan Construction Law p.a.</span>
    </div>
  </section>

  <div class="bottom-strip"></div>
</main>
</body>
</html>
```